I need a flyer that is professional, advertises and informs people about my health coaching practice. I am a Nationally Board Certified Health and Wellness Coach, lifestyle medicine certified and a lifestyle coach for the NHQ's Glucose Steady Initiative. I have my Master's Degree in Counseling Psychology. The final design should communicate evidence based health coaching that is self-directed and aimed at creating lasting health behavioral changes designed to enhance well-being. I am very open in terms of design but really would like a professional look to the flyer. I did want my contact information on the flyer: dana@vitalpathrecords.com and (217) 555-0148

Target Market(s)

Adults looking to improve their health, decrease risk factors for lifestyle disease, reduce weight, make better lifestyle choices to improve well-being.

Industry/Entity Type

Health And Wellness

Font styles to use
Sans Serif

Colors

Designer to choose colors to be used in the design.

Requirements
Must have
• Services offered, a professional feel, Dana Morrow Health Coaching (name of my practice), my phone number (217) 555-0148 and email: dana@vitalpathrecords.com, location: 1873 W Larkfield Avenue Bloomington IL 61709 my website: danamorrow.com to schedule appointments
Nice to have
• What is Health Coaching? Health and Wellness Coaches partner with clients seeking self-directed, lasting changes, aligned with their values, which promote health and wellness and, thereby, enhance well-being. In the course of their work health and wellness coaches display unconditional positive regard for their clients and a belief in their capacity for change, and honoring that each client is an expert on his or her life, while ensuring that all interactions are respectful and non-judgmental.

```html
<!DOCTYPE html>
<html lang="en">
<head>
<meta charset="utf-8">
<title>Dana Morrow Health Coaching</title>
<link rel="stylesheet" href="https://fonts.googleapis.com/css2?family=Montserrat:wght@700;800&family=Open+Sans:wght@400;600;700&family=Roboto+Slab:wght@400&display=swap">
<style>
  :root {
    --brand-blue: #4a7cc4;
    --brand-blue-dark: #2f5fa8;
    --ink: #2b2b33;
    --sky-top: #dfeefa;
    --sky-mid: #cfe6f7;
    --sky-low: #e8f1fb;
    --panel: rgba(255, 255, 255, 0.55);
    --frame: #a9c6e8;
    --white: #ffffff;
  }
  * { box-sizing: border-box; margin: 0; padding: 0; }
  html, body { width: 801px; height: 1200px; overflow: hidden; background: #ffffff; }
  .flyer {
    position: relative;
    width: 801px;
    height: 1200px;
    overflow: hidden;
    font-family: "Open Sans", Arial, sans-serif;
    color: var(--ink);
    background:
      radial-gradient(circle at 12% 22%, rgba(255,255,255,0.8) 0 40px, transparent 70px),
      radial-gradient(circle at 55% 40%, rgba(255,255,255,0.55) 0 30px, transparent 60px),
      radial-gradient(circle at 30% 60%, rgba(255,240,215,0.6) 0 50px, transparent 90px),
      radial-gradient(circle at 70% 78%, rgba(255,255,255,0.6) 0 40px, transparent 80px),
      linear-gradient(180deg, var(--sky-top) 0%, var(--sky-mid) 45%, #d6e4f4 70%, var(--sky-low) 100%);
  }
  .masthead {
    position: absolute; left: 195px; top: 0; width: 403px; height: 157px;
    background: var(--brand-blue);
    display: flex; align-items: center; justify-content: center; text-align: center;
  }
  .masthead h1 {
    font-family: "Montserrat", Arial, sans-serif; font-weight: 800;
    color: var(--white); font-size: 38px; line-height: 44px; letter-spacing: 1px;
  }
  .photo { position: absolute; }
  .photo-couple-top {
    left: 511px; top: 130px; width: 290px; height: 274px;
    background: radial-gradient(ellipse at 50% 55%, #f1ece6 0%, #d9c2ad 40%, rgba(207,230,247,0) 75%);
  }
  .photo-couple-senior {
    left: 61px; top: 801px; width: 298px; height: 252px;
    background: radial-gradient(ellipse at 50% 50%, #e9dccf 0%, #c9d6e8 55%, rgba(207,230,247,0) 78%);
  }
  .photo-lotus {
    left: 557px; top: 900px; width: 244px; height: 300px;
    background: radial-gradient(ellipse at 55% 55%, #f6b3c8 0%, #f2cbd7 40%, rgba(232,241,251,0) 75%);
  }
  .tagline {
    position: absolute; left: 70px; top: 218px; width: 450px; text-align: center;
    font-family: "Roboto Slab", Georgia, serif; color: var(--brand-blue);
    font-size: 29px; line-height: 34px;
  }
  .subline {
    position: absolute; left: 23px; top: 292px;
    font-family: "Open Sans", Arial, sans-serif; font-weight: 700;
    color: var(--brand-blue); font-size: 16px; letter-spacing: 1.2px;
  }
  .services { position: absolute; left: 15px; top: 402px; width: 400px; }
  .service { position: absolute; left: 0; width: 400px; }
  .service h2 {
    display: inline-block;
    font-family: "Open Sans", Arial, sans-serif; font-weight: 700;
    font-size: 19px; line-height: 24px; color: var(--white);
    background: var(--brand-blue); padding: 0 10px 0 4px;
    border-radius: 0 12px 12px 0;
  }
  .service h2 small { font-size: 13px; }
  .service p { font-size: 15.5px; line-height: 23px; margin-left: 4px; color: var(--ink); }
  .service .first { margin-top: 7px; }
  .about {
    position: absolute; left: 497px; top: 404px; width: 304px; height: 443px;
    border: 4px solid var(--frame); border-right: none;
    background: var(--panel);
    padding: 10px 10px 10px 14px;
  }
  .about h3 {
    font-family: "Roboto Slab", Georgia, serif; font-weight: 400;
    color: var(--brand-blue); font-size: 23px; line-height: 27px; text-align: center;
  }
  .about p {
    margin-top: 6px; font-size: 15.5px; line-height: 22px; text-align: justify;
    hyphens: auto; color: var(--ink);
  }
  .contact { position: absolute; left: 18px; top: 1056px; }
  .contact-line {
    display: flex; align-items: center; gap: 10px; height: 34px;
    font-weight: 700; font-size: 18px; color: var(--brand-blue-dark);
  }
  .contact-line svg { width: 24px; height: 24px; flex: none; }
  .web-bar {
    position: absolute; left: 221px; top: 1157px; width: 359px; height: 43px;
    background: var(--brand-blue); color: var(--white);
    display: flex; align-items: center; justify-content: center;
    font-family: "Open Sans", Arial, sans-serif; font-weight: 700; font-size: 26px;
  }
</style>
</head>
<body>
<main class="flyer">
  <header class="masthead">
    <h1>DANA MORROW<br>HEALTH COACHING</h1>
  </header>

  <div class="photo photo-couple-top" role="img" aria-label="Photo of a happy young couple, arms spread, against a bright sky"></div>

  <p class="tagline">Health coaching is<br>embracing your health</p>
  <p class="subline">Let us help you build the healthy life you deserve</p>

  <section class="services">
    <div class="service" style="top:0">
      <h2>Health Coaching Initial Consultation</h2>
      <p class="first">Health Coaching Data Collection ...(1 hr | $199)</p>
      <p>Health Coaching Initial Consultation (30min | free)</p>
    </div>
    <div class="service" style="top:98px">
      <h2>Health Coaching Individual <small>30 Minute Session</small></h2>
      <p class="first">Individual Health Coaching<br>30 Minute Session .................... (30min | $50)</p>
    </div>
    <div class="service" style="top:194px">
      <h2>Health Coaching 6 Session Package</h2>
      <p class="first">Health Coaching Package<br>Six 30 Minute Sessions ............ (30min | $275)</p>
    </div>
    <div class="service" style="top:270px">
      <h2>16 Week NHQ Diabetes Prevention<br>Program - Steady Start</h2>
      <p class="first">NHQ Steady Start Type 2 Diabetes Lifestyle<br>16 Week Program ................... (30min | $249)</p>
    </div>
  </section>

  <aside class="about">
    <h3>What is<br>Health Coaching?</h3>
    <p>Health and Wellness Coaches partner with clients seeking self-directed, lasting changes, aligned with their values, which promote health and wellness and, thereby, enhance well-being. In the course of their work health and wellness coaches display unconditional positive regard for their clients and a belief in their capacity for change, and honoring that each client is an expert on his or her life, while ensuring that all interactions are respectful and non-judgmental.</p>
  </aside>

  <div class="photo photo-couple-senior" role="img" aria-label="Photo of a smiling senior couple embracing"></div>
  <div class="photo photo-lotus" role="img" aria-label="Photo of a pink lotus flower"></div>

  <address class="contact" style="font-style:normal">
    <div class="contact-line">
      <svg viewBox="0 0 24 24" aria-hidden="true"><circle cx="12" cy="12" r="12" fill="#2f5fa8"/><path d="M8.2 6.5l2 0 1 3-1.3 1.1a8 8 0 0 0 3.5 3.5l1.1-1.3 3 1v2a1.2 1.2 0 0 1-1.3 1.2A10 10 0 0 1 7 7.8 1.2 1.2 0 0 1 8.2 6.5z" fill="#fff"/></svg>
      <span>(217) 555-0148</span>
    </div>
    <div class="contact-line">
      <svg viewBox="0 0 24 24" aria-hidden="true"><circle cx="12" cy="12" r="12" fill="#2f5fa8"/><rect x="6" y="8" width="12" height="8.5" rx="1" fill="#fff"/><path d="M6.5 8.5l5.5 4.3 5.5-4.3" fill="none" stroke="#2f5fa8" stroke-width="1.3"/></svg>
      <span>dana@vitalpathrecords.com</span>
    </div>
    <div class="contact-line">
      <svg viewBox="0 0 24 24" aria-hidden="true"><circle cx="12" cy="12" r="12" fill="#2f5fa8"/><path d="M12 5a4.5 4.5 0 0 1 4.5 4.5c0 3.3-4.5 8.5-4.5 8.5s-4.5-5.2-4.5-8.5A4.5 4.5 0 0 1 12 5z" fill="#fff"/><circle cx="12" cy="9.6" r="1.7" fill="#2f5fa8"/></svg>
      <span>1873 W Larkfield Avenue Bloomington IL 61709</span>
    </div>
  </address>

  <footer class="web-bar">danamorrow.com</footer>
</main>
</body>
</html>
```